Business Card

I need a business card that really pops for a potential customer or person who refers a personal injury lead. I want to highlight our office locations, but only address that needs to be on the card is my office's main address. I want a sleek, modern and minimalist design.

```html
<!DOCTYPE html>
<html lang="en">
<head>
<meta charset="utf-8">
<title>Northline Injury Lawyers – Business Card</title>
<link rel="stylesheet" href="https://fonts.googleapis.com/css2?family=Arimo:wght@400;700&display=swap">
<style>
  :root {
    --backdrop: #7a7a7a;
    --card-dark: #373737;
    --card-light: #f7f7f7;
    --ink: #222222;
    --ink-soft: #6b6b6b;
    --logo-dark: #9a9a9a;
    --on-dark: #e6e6e6;
    --rule: #9b9b9b;
  }
  * { margin: 0; padding: 0; box-sizing: border-box; }
  html, body { width: 1200px; height: 900px; overflow: hidden; }
  body {
    background: var(--backdrop);
    font-family: "Arimo", Arial, sans-serif;
    position: relative;
  }
  .card {
    position: absolute;
    width: 630px;
    height: 360px;
    border-radius: 22px;
    box-shadow: 0 10px 24px rgba(0,0,0,0.25);
  }
  .card--front { left: 200px; top: 70px; background: var(--card-dark); }
  .card--back  { left: 370px; top: 470px; background: var(--card-light); color: var(--ink); }

  .wordmark { text-transform: uppercase; font-weight: 400; line-height: 1; }
  .wordmark__main { display: block; letter-spacing: 0.16em; }
  .wordmark__sub  { display: block; letter-spacing: 0.52em; }

  .card--front .wordmark {
    position: absolute; left: 0; right: 0; top: 110px;
    text-align: center; color: var(--logo-dark);
  }
  .card--front .wordmark__main { font-size: 58px; }
  .card--front .wordmark__sub  { font-size: 20px; margin-top: 10px; }
  .card--front .site {
    position: absolute; left: 0; right: 0; bottom: 48px;
    text-align: center; color: var(--on-dark);
    font-size: 15px; letter-spacing: 0.22em;
  }

  .card--back .wordmark {
    position: absolute; right: 38px; top: 40px;
    text-align: right; color: var(--ink);
  }
  .card--back .wordmark__main { font-size: 38px; }
  .card--back .wordmark__sub  { font-size: 13px; margin-top: 7px; }

  .person { position: absolute; left: 40px; bottom: 44px; }
  .person__name { font-size: 24px; font-weight: 700; }
  .person__role { font-size: 15px; color: var(--ink-soft); margin-top: 3px; }
  .person__address { font-size: 16px; line-height: 1.3; margin-top: 14px; }
  .contact-list { list-style: none; margin-top: 18px; font-size: 16px; line-height: 1.4; }
  .contact-list li { display: flex; align-items: center; gap: 8px; }
  .contact-list svg { width: 14px; height: 14px; fill: var(--ink); flex: none; }

  .divider {
    position: absolute; left: 316px; bottom: 50px;
    width: 1px; height: 90px; background: var(--rule);
  }
  .online { position: absolute; left: 334px; bottom: 96px; }
</style>
</head>
<body>

<section class="card card--front" aria-label="Card front">
  <div class="wordmark">
    <span class="wordmark__main">Northline</span>
    <span class="wordmark__sub">Injury Lawyers</span>
  </div>
  <p class="site">www.northlineinjurylawyers.com</p>
</section>

<section class="card card--back" aria-label="Card back">
  <div class="wordmark">
    <span class="wordmark__main">Northline</span>
    <span class="wordmark__sub">Injury Lawyers</span>
  </div>

  <div class="person">
    <h1 class="person__name">Daniel Brooks</h1>
    <p class="person__role">Lawyer</p>
    <p class="person__address">240 Harbor Street<br>Suite 1800, Chicago, IL 60611</p>
    <ul class="contact-list">
      <li>
        <svg viewBox="0 0 24 24" aria-hidden="true"><path d="M6.6 10.8a15.1 15.1 0 0 0 6.6 6.6l2.2-2.2c.3-.3.7-.4 1-.2 1.1.4 2.3.6 3.6.6.6 0 1 .4 1 1V20c0 .6-.4 1-1 1A17 17 0 0 1 3 4c0-.6.4-1 1-1h3.5c.6 0 1 .4 1 1 0 1.3.2 2.5.6 3.6.1.3 0 .7-.2 1z"/></svg>
        312-555-0148
      </li>
      <li>
        <svg viewBox="0 0 24 24" aria-hidden="true"><path d="M3 3h18v14H8l-5 4z"/></svg>
        312-555-0172
      </li>
    </ul>
  </div>

  <div class="divider"></div>

  <ul class="contact-list online">
    <li>
      <svg viewBox="0 0 24 24" aria-hidden="true"><path d="M2 5h20v14H2zm2 2v.4l8 5 8-5V7z"/></svg>
      info@northlineinjurylawyers.com
    </li>
    <li>
      <svg viewBox="0 0 24 24" aria-hidden="true"><circle cx="12" cy="12" r="10"/></svg>
      northlineinjurylawyers.com
    </li>
  </ul>
</section>

</body>
</html>
```